Creative and elegant Brochure Design Project

Graceful Summonly, a online platform to design and sen out online invitations, track RSVP, create seating charts, place cards, thank you cards as well as a gift registry.
Should have clean and elegant outer sides, with more informative inner sides, like features, or pricing, or other information that can be found both on the website and the articles attached.
can include something like: Graceful Summonly is more than just a way to create simple elegant invitations. It is a whole suite of event management tools.
UNIQUE EDITABLE DESIGNS
INSTANT RSVP'S
LAST MINUTE INVITES
GUEST MANAGEMENT TOOLS
AUTOMATED SEATING CHARTS AND PLACE CARDS
CALENDAR INTEGRATION AND MESSAGING
AUTOMATED THANK YOU CARDS
GIFT REGISTRY
OPTIONAL PRINTED POSTCARDS
Industry/Entity Type
Event Planning
Colors
Designer to choose colors to be used in the design.
Look and feel
Each slider illustrates characteristics of the customer's brand and the style your logo design should communicate.

```html
<!DOCTYPE html>
<html lang="en">
<head>
<meta charset="utf-8">
<title>Graceful Summonly – Trifold Brochure</title>
<link href="https://fonts.googleapis.com/css2?family=Cinzel:wght@400&family=Cormorant+Garamond:wght@400;500&family=Open+Sans:wdth,wght@75..100,400&family=Roboto:wght@400&display=swap" rel="stylesheet">
<style>
  :root{
    --backdrop:#f1efec;
    --paper:#ffffff;
    --fold:#ececec;
    --gold:#b39a62;
    --gold-soft:#c9b68a;
    --rule:#ddd6c8;
    --ink:#3a3a3a;
    --photo-grey:#d9dbe0;
    --photo-blush:#ecd8cf;
    --photo-cream:#f3ede2;
  }
  *{margin:0;padding:0;box-sizing:border-box}
  html,body{width:802px;height:1200px;overflow:hidden}
  body{background:var(--backdrop);position:relative;font-family:"Open Sans",sans-serif}

  .spread{position:absolute;left:62px;width:678px;height:524px;display:flex;box-shadow:0 2px 10px rgba(0,0,0,.12)}
  .spread--outer{top:62px}
  .spread--inner{top:615px}
  .panel{position:relative;width:226px;height:100%;background:var(--paper);overflow:hidden}
  .panel--folded{background:linear-gradient(90deg,#fff 0%,#fff 55%,var(--fold) 100%)}

  .photo{position:absolute;left:0;width:100%}
  .photo--invites-grey{top:0;height:196px;background:
      linear-gradient(180deg,rgba(255,255,255,0) 55%,#fff 100%),
      linear-gradient(135deg,var(--photo-grey) 0%,var(--photo-cream) 45%,var(--photo-grey) 75%,#efe6d2 100%)}
  .photo--invites-blush{top:120px;height:252px;background:
      linear-gradient(180deg,rgba(255,255,255,0) 65%,#fff 100%),
      linear-gradient(140deg,var(--photo-blush) 0%,#f6efe6 40%,var(--photo-blush) 70%,#cfd8c4 100%)}
  .photo--table-card{top:0;height:190px;background:
      linear-gradient(180deg,rgba(255,255,255,0) 60%,#fff 100%),
      linear-gradient(150deg,var(--photo-blush) 0%,#f5f1ea 45%,var(--photo-grey) 80%,var(--photo-cream) 100%)}

  .brand{display:flex;align-items:center;justify-content:center;gap:6px;color:var(--gold);font-family:"Roboto",sans-serif;letter-spacing:.06em;text-transform:uppercase}
  .brand__dot{width:6px;height:6px;border-radius:50%;background:var(--gold)}

  .intro-title{position:absolute;top:204px;width:100%;text-align:center;font-family:"Cormorant Garamond",serif;font-size:17px;color:var(--gold)}
  .intro-brand{position:absolute;top:235px;width:100%;font-size:6.5px}
  .features{position:absolute;top:276px;left:25px;width:175px;list-style:none}
  .features li{border-bottom:1px solid var(--rule);text-align:center;font-family:"Roboto",sans-serif;font-size:8.4px;line-height:11px;color:var(--gold);padding:5.6px 0}
  .features li:last-child{border-bottom:none}

  .tagline{position:absolute;top:218px;width:100%;text-align:center;font-family:"Cinzel",serif;font-size:16px;line-height:21px;color:var(--gold)}
  .tagline-brand{position:absolute;top:286px;width:100%;font-size:8.5px}
  .contact{position:absolute;top:422px;width:100%;text-align:center;font-family:"Roboto",sans-serif;font-size:8.6px;line-height:15px;color:var(--gold)}
  .contact svg{display:block;margin:0 auto 4px}

  .cover-brand{position:absolute;top:60px;width:100%;font-size:10px}
  .cover-rule{position:absolute;top:113px;left:0;width:100%;height:2px;background:var(--gold-soft)}
  .cover-title{position:absolute;top:408px;width:100%;text-align:center;font-family:"Cinzel",serif;font-size:15.5px;line-height:21px;color:var(--gold)}

  .copy{position:absolute;left:25px;width:176px;font-family:"Open Sans",sans-serif;font-stretch:80%;font-size:7px;line-height:10.4px;color:var(--ink);text-align:justify}
  .copy p{margin-bottom:10.4px}
  .copy p.tight{margin-bottom:0}
  .copy--top{top:40px}
  .copy--after-photo{top:173px}
</style>
</head>
<body>

<section class="spread spread--outer">
  <div class="panel panel--folded">
    <div class="photo photo--invites-grey" role="img" aria-label="Photo of gold-trimmed wedding invitation cards on grey linen with cream flowers"></div>
    <h2 class="intro-title">Invitations Made Easy.</h2>
    <div class="brand intro-brand"><span>Graceful Summonly</span><span class="brand__dot"></span></div>
    <ul class="features">
      <li>UNIQUE EDITABLE DESIGNS</li>
      <li>INSTANT RSVP'S</li>
      <li>LAST MINUTE INVITES</li>
      <li>GUEST MANAGEMENT TOOLS</li>
      <li>AUTOMATED SEATING CHARTS AND PLACE CARDS</li>
      <li>CALENDAR INTEGRATION AND MESSAGING</li>
      <li>AUTOMATED THANK YOU CARDS</li>
      <li>GIFT REGISTRY</li>
      <li>OPTIONAL PRINTED POSTCARDS</li>
    </ul>
  </div>

  <div class="panel panel--folded">
    <h2 class="tagline">Just the joy.<br>None of the stress.</h2>
    <div class="brand tagline-brand"><span>Graceful Summonly</span><span class="brand__dot"></span></div>
    <div class="contact">
      <svg width="16" height="16" viewBox="0 0 16 16" aria-hidden="true">
        <circle cx="8" cy="8" r="7.2" fill="none" stroke="var(--gold)" stroke-width="1"/>
        <path d="M5.3 4.6c.4-.3.8-.3 1 .1l.7 1.2c.2.3.1.7-.2.9l-.4.3c.4.9 1.1 1.7 2 2.2l.3-.4c.2-.3.6-.4.9-.2l1.2.7c.4.2.4.7.1 1l-.5.5c-.5.5-1.4.5-2.3 0-1.5-.8-2.8-2.1-3.5-3.6-.4-.9-.3-1.8.2-2.2z" fill="var(--gold)"/>
      </svg>
      +1 800 555 0142<br>GracefulSummonly.com
    </div>
  </div>

  <div class="panel">
    <div class="brand cover-brand"><span>Graceful Summonly</span><span class="brand__dot"></span></div>
    <div class="cover-rule"></div>
    <div class="photo photo--invites-blush" role="img" aria-label="Photo of a blush pocket-fold wedding invitation with gold frame and greenery"></div>
    <h1 class="cover-title">Invitations And<br>Party-Planning Enter<br>The Digital Age</h1>
  </div>
</section>

<section class="spread spread--inner">
  <div class="panel panel--folded">
    <div class="copy copy--top">
      <p class="tight">The glass breaks and the music plays and the crowd surges forward to say mazel tov to the chassan and kallah. The bar mitzvah bachur finishes his drasha to the acclaim of all the guests. Simchas are supposed to be happy occasions, and we wait for the beautiful highlights and emotional moments.</p>
      <p>But the actual experience can be nerve-wracking and frustrating, when you're trying to juggle all of the tasks needed to actually get the simcha off the ground, including inviting guests, seating them, and making sure you'll thank them afterwards.</p>
      <p class="tight">You need to worry about getting the text you'll be using to a print shop. If you're addressing your own envelopes, you'll need to figure out how to align labels on your home printer. (How many misprinted sheets have you thrown out already?) You need to deal with every hassle involved in mailing them: stamping them, licking envelopes, getting a huge pile or several boxes of invitations to the post office. But even then, you're not done. You need to wait for your invitations to travel by snail mail to your guests' homes. Hopefully, they'll receive them, eventually open them, and maybe remember to send back the RSVP cards, making their own way to a mailbox. Those, too, have to make their way through the postal system and eventually come back, clogging your mail slot. And then comes the mind-numbing chore of opening each envelope, deciphering the handwriting, and marking down the guests' choices.</p>
      <p class="tight">After that, you'll need to get out your seating chart, find your list of attendees (hope you haven't misplaced that), and start figuring out, painstakingly, where everyone goes.</p>
      <p class="tight">At one time, planning a Jewish wedding meant sending invitations out of town on a donkey-driven wagon. Sometimes it feels like the process hasn't really advanced all that much since then. But in fact, today it's possible to get everything you need done easily, all in one place, with the new innovative service Graceful Summonly. Your entire guest list gets entered online, using a simple interface. You send out the invitations, not by standing in line at the post office, but by</p>
    </div>
  </div>

  <div class="panel panel--folded">
    <div class="photo photo--table-card" role="img" aria-label="Photo of a gold-lettered table number card among blush envelopes and cream flowers"></div>
    <div class="copy copy--after-photo">
      <p>pressing Enter on your keyboard, with a choice of numerous uniquely designed and editable invitations to choose from. Your guests will receive their invitations immediately, and they can't misplace them. And RSVPing is easy for them; they do it right from their own computers.</p>
      <p>That guest list doesn't just serve as the basis for the electronic invitations. Graceful Summonly lets you arrange your seating charts, create place cards, and generate thank-you cards for gifts with just the click of a button. You won't be juggling reams of papers and numerous lists; everything is right there online. No one is left out; no one is forgotten; no one is hurt because they haven't received an invitation, a place setting, or a thank you card.</p>
      <p>And that also means that your event is a pleasure for your guests. Rather than a pile of invitations sitting on their kitchen table or hung on their fridge, they have an ability to receive and review your invitation with no hassle. They never lose the invitations, which are always available electronically. They won't forget to attend your events or be unable to remember where they will be taking place.</p>
      <p>Graceful Summonly also provides an online gift registry, so that when they RSVP for your event, they can instantly choose the gift they will be giving to the chasan and kallah, whether they are able to attend the</p>
    </div>
  </div>

  <div class="panel">
    <div class="copy copy--top">
      <p>wedding or not. That makes both the gift-giving easy for guests and also means that the chasan and kallah will likely receive more gifts from those who would like to give but are stymied by the logistics.</p>
      <p>With standard invitations alone for a moderate-sized wedding costing at the very least $2,000 and likely much more, the savings of using Graceful Summonly is substantial, while you can have the elegance and exclusive designs that only incredibly expensive printed invitations would supply, but with all of the control that printed invitations never can.</p>
      <p>The low cost also means that you can use the elegance and custom features of Graceful Summonly for smaller events, like bar and bat mitzvahs, baby birth events, and engagements, to create a smoother experience and a better and bigger gift registry.</p>
      <p>For those who aren't willing or able to leave print entirely behind, Graceful Summonly also has several options. When you want to use print invitations for all of your guests, our RSVP service allows you to utilize the digital enhancements of Graceful Summonly, like seating chart creation, place card automation, and thank you card production, to make everything happen easily and the way you want it and save money at the same time. And because the RSVPing happens online, there's no wait for return cards to make their way back to you. You'll know who is coming right away, and your seating charts and place cards can be made right from that list.</p>
      <p>Furthermore, if most of your guests are fine with receiving digital invitations but you have a few who would really appreciate a paper invitation, we can print them for you.</p>
      <p>The invitation of the past may have headed out on the back of the wagon, but there's no good reason you should be stuck there. The modern age has arrived, and it will make your simcha a truly happy one.</p>
    </div>
  </div>
</section>

</body>
</html>
```